Number of Pages Required

1 page

Requirements
Must have
• An Overview / Background of the Business & Services(not for profit rescue animal farm)
• The Target Market / Audience you are trying to reach (animal lovers)
• Design Specifics; any preferences or ideas for Style, Colour, Imagery, etc (no preferences)

```html
<!DOCTYPE html>
<html lang="en">
<head>
<meta charset="utf-8">
<title>We Love Animals</title>
<link rel="stylesheet" href="https://fonts.googleapis.com/css2?family=Courgette&family=Nunito+Sans:wght@400;700;800&family=Open+Sans:wght@400&display=swap">
<style>
  :root {
    --page: #ffffff;
    --nav: #fd5252;
    --nav-active: #0b9f7d;
    --nav-text: #ffffff;
    --section: #f1f1f1;
    --ink: #111111;
    --body-text: #5a5a5a;
    --rule: #dcdcdc;
    --ring: #ffffff;
    --footer-edge: #252525;
  }
  * { margin: 0; padding: 0; box-sizing: border-box; }
  html, body {
    width: 1200px; height: 1000px; overflow: hidden; background: var(--page);
  }
  .site { position: relative; width: 1200px; height: 1000px; }

  .main-nav {
    position: absolute; top: 72px; left: 0; width: 1200px; height: 68px;
    background: var(--nav);
  }
  .main-nav a {
    position: absolute; top: 0; height: 68px; line-height: 68px;
    color: var(--nav-text); text-decoration: none;
    font-family: "Nunito Sans", sans-serif; font-size: 15px; letter-spacing: 0.2px;
  }
  .main-nav a.is-active {
    background: var(--nav-active); padding: 0 17px;
  }

  .team-section {
    position: absolute; top: 140px; left: 0; width: 1200px; height: 782px;
    background: var(--section);
  }
  .section-title {
    position: absolute; top: 92px; left: 0; width: 1226px; text-align: center;
    font-family: "Courgette", cursive; font-weight: 400; font-size: 57px;
    color: var(--ink); line-height: 1;
  }
  .title-rule {
    position: absolute; top: 197px; left: 503px; width: 219px; height: 1px;
    background: var(--rule);
  }
  .pet-mark {
    position: absolute; width: 26px; height: 24px;
  }
  .title-mark { top: 176px; left: 604px; }
  .divider-mark { top: 436px; left: 601px; }

  .dotted-divider { position: absolute; top: 435px; left: 0; }

  .member-photo {
    position: absolute; top: 294px; width: 300px; height: 300px; border-radius: 50%;
    border: 9px solid var(--ring);
    box-shadow: 0 0 3px rgba(0,0,0,0.06);
  }
  .photo-left {
    left: 187px;
    background: radial-gradient(circle at 60% 40%, #b9bec4 0%, #8e9296 45%, #6f706c 100%);
  }
  .photo-right {
    left: 746px;
    background: radial-gradient(circle at 45% 30%, #e9c9b0 0%, #c98b4c 45%, #9a6a3a 80%, #8fc4d0 100%);
  }

  .member {
    position: absolute; top: 642px; width: 400px; text-align: center;
  }
  .member-left { left: 130px; }
  .member-right { left: 696px; }
  .member-name {
    font-family: "Nunito Sans", sans-serif; font-weight: 400; font-size: 29px;
    color: var(--ink); line-height: 1.1;
  }
  .member-name strong { font-weight: 800; }
  .member-bio {
    margin-top: 24px;
    font-family: "Open Sans", sans-serif; font-size: 14.5px; line-height: 28px;
    color: var(--body-text);
  }

  .footer-edge {
    position: absolute; top: 922px; left: 0; width: 1200px; height: 5px;
    background: var(--footer-edge);
  }
</style>
</head>
<body>
<div class="site">
  <nav class="main-nav">
    <a class="is-active" href="#" style="left:130px;">Home</a>
    <a href="#" style="left:246px;">About Us</a>
    <a href="#" style="left:368px;">Our Story</a>
    <a href="#" style="left:493px;">Our Animals</a>
    <a href="#" style="left:629px;">Events</a>
    <a href="#" style="left:731px;">Gallery</a>
    <a href="#" style="left:833px;">Blog</a>
  </nav>

  <section class="team-section">
    <h1 class="section-title">We Love Animals</h1>
    <div class="title-rule"></div>
    <svg class="pet-mark title-mark" role="img" aria-label="Small cat icon" viewBox="0 0 26 24">
      <ellipse cx="13" cy="14" rx="10" ry="8" fill="var(--ink)"/>
    </svg>

    <svg class="dotted-divider" width="1200" height="30" viewBox="0 0 1200 30">
      <g fill="#ffffff">
        <circle cx="131" cy="10" r="2.5"/><circle cx="149" cy="10" r="4"/><circle cx="166" cy="10" r="2.5"/>
        <circle cx="497" cy="10" r="2.5"/><circle cx="514" cy="10" r="4"/><circle cx="531" cy="10" r="2.5"/>
        <circle cx="547" cy="10" r="2.5"/><circle cx="563" cy="10" r="3"/><circle cx="582" cy="10" r="4"/>
        <circle cx="646" cy="10" r="4"/><circle cx="664" cy="10" r="3"/><circle cx="683" cy="10" r="4"/>
        <circle cx="700" cy="10" r="2.5"/><circle cx="716" cy="10" r="2.5"/><circle cx="731" cy="10" r="2.5"/>
        <circle cx="1060" cy="10" r="2.5"/><circle cx="1077" cy="10" r="4"/><circle cx="1094" cy="10" r="2.5"/>
      </g>
    </svg>
    <svg class="pet-mark divider-mark" role="img" aria-label="Small cat icon" viewBox="0 0 26 24">
      <ellipse cx="13" cy="14" rx="10" ry="8" fill="var(--ink)"/>
    </svg>

    <div class="member-photo photo-left" role="img" aria-label="Portrait photo of Owen Hale seated outdoors"></div>
    <div class="member-photo photo-right" role="img" aria-label="Photo of Nora Bell smiling with a golden retriever and a kitten"></div>

    <div class="member member-left">
      <h2 class="member-name"><strong>Owen</strong> Hale</h2>
      <p class="member-bio">Lorem ipsum dolor sit amet, consectetur adipiscing<br>elit, sed do eiusmod tempor incididunt ut<br>abore et dolore magna aliqua.</p>
    </div>
    <div class="member member-right">
      <h2 class="member-name"><strong>Nora</strong> Bell</h2>
      <p class="member-bio">Lorem ipsum dolor sit amet, consectetur adipiscing<br>elit, sed do eiusmod tempor incididunt ut<br>labore et dolore magna aliqua.</p>
    </div>
  </section>

  <div class="footer-edge"></div>
</div>
</body>
</html>
```